Stylish Business Card for Modern hair salon

I need a simple business card design using our salon logo and colours that are in the logo. We service clients of all ages but predominantly those in the 18 to 55 age range. We have a young staff and are looking to have a card that will present a modern and clean image that represents who we are. The card should be in black and white same as our logo. Minimal use of other colours is allowed.

Industry/Entity Type

Hair And Beauty

Contact Information for Business Card

The design should have the following information
salon name - TR Hair Studio
address - 2751 Birchfield Rd.E. Mississauga, ON L7P3K2
phone - 905 614-2870
website - trhairexample.ca
instagram - tr.hairstudio
twitter - @TR_HairStudio

Colors
000000
ffffff
474747

Requirements
Must have
• simple design, salon name, address, phone, website, instagram, twitter info
• Back of card should have the following:
• YOUR NEXT APPOINTMENT
• DATE
• TIME
Nice to have
• simple design, clear to see and read,
• predominantly black and white colour, minimal use of other colours is ok
Should not have
• many colours, various fonts

```html
<!DOCTYPE html>
<html lang="en">
<head>
<meta charset="utf-8">
<title>TR Hair Studio – Business Card</title>
<link href="https://fonts.googleapis.com/css2?family=Bodoni+Moda:wght@400;500;700&display=swap" rel="stylesheet">
<style>
  :root {
    --ink: #000000;
    --paper: #ffffff;
    --grey: #474747;
    --backdrop: #d9d9d9;
    --rule-light: #9a9a9a;
  }
  * { margin: 0; padding: 0; box-sizing: border-box; }
  html, body {
    width: 1200px; height: 1200px; overflow: hidden;
    background: var(--backdrop);
    font-family: "Bodoni Moda", "Times New Roman", serif;
  }
  .canvas { position: relative; width: 1200px; height: 1200px; }

  .card {
    position: absolute; top: 435px;
    width: 552px; height: 330px;
    box-shadow: 0 2px 8px rgba(0,0,0,0.18);
  }
  .card--front { left: 30px; background: var(--ink); color: var(--paper); }
  .card--back { left: 618px; background: var(--paper); color: var(--ink); }

  .wordmark {
    position: absolute;
    font-weight: 500; font-size: 50px; letter-spacing: 2px;
    line-height: 1; white-space: nowrap;
  }
  .card--front .wordmark { left: 28px; top: 38px; color: var(--paper); }
  .card--back .wordmark { left: 0; right: 0; top: 48px; text-align: center; color: var(--ink); }

  .studio-name {
    position: absolute; left: 284px; top: 110px;
    font-size: 21px; font-weight: 700; letter-spacing: 0.5px;
    text-transform: uppercase; white-space: nowrap;
  }
  .studio-rule {
    position: absolute; left: 278px; right: 0; top: 142px;
    height: 1px; background: var(--paper);
  }
  .section-rule {
    position: absolute; left: 0; width: 456px; top: 168px;
    height: 1px; background: var(--rule-light);
  }

  .contact-list {
    position: absolute; left: 24px; top: 182px; list-style: none;
  }
  .contact-list li {
    display: flex; align-items: center; height: 26.5px;
    font-size: 15px; text-transform: uppercase; letter-spacing: 0.3px;
  }
  .contact-list svg { width: 14px; height: 14px; margin-right: 16px; flex: none; }

  .appointment-title {
    position: absolute; left: 0; right: 0; top: 186px;
    text-align: center; font-size: 19px; font-weight: 700;
    letter-spacing: 0.3px; text-transform: uppercase;
  }
  .appointment-rule { position: absolute; left: 124px; top: 208px; width: 304px; height: 10px; }

  .slot {
    position: absolute; top: 272px;
    font-size: 16px; text-transform: uppercase;
    display: flex; align-items: baseline; white-space: nowrap;
  }
  .slot--date { left: 46px; }
  .slot--time { left: 290px; }
  .slot__line {
    display: inline-block; height: 1px; margin-left: 6px;
    border-bottom: 2px dotted var(--ink);
  }
  .slot--date .slot__line { width: 148px; }
  .slot--time .slot__line { width: 150px; }
</style>
</head>
<body>
<main class="canvas">

  <section class="card card--front" aria-label="Front of business card">
    <div class="wordmark">TR HAIR</div>
    <div class="studio-name">TR Hair Studio</div>
    <div class="studio-rule"></div>
    <div class="section-rule"></div>
    <ul class="contact-list">
      <li>
        <svg viewBox="0 0 14 14" aria-hidden="true"><rect x="0.5" y="0.5" width="13" height="13" fill="none" stroke="#fff"/><path d="M7 3a2.5 2.5 0 0 0-2.5 2.5C4.5 7.5 7 11 7 11s2.5-3.5 2.5-5.5A2.5 2.5 0 0 0 7 3z" fill="#fff"/><circle cx="7" cy="5.5" r="0.9" fill="#000"/></svg>
        2751 Birchfield Rd.E. Mississauga, ON L7P3K2
      </li>
      <li>
        <svg viewBox="0 0 14 14" aria-hidden="true"><rect x="0.5" y="0.5" width="13" height="13" fill="none" stroke="#fff"/><path d="M4.2 3.5l1.6-.3 1 2-1 .8a5 5 0 0 0 2.2 2.2l.8-1 2 1-.3 1.6c-3.4.2-6.5-2.9-6.3-6.3z" fill="#fff"/></svg>
        905 614-2870
      </li>
      <li>
        <svg viewBox="0 0 14 14" aria-hidden="true"><rect x="0.5" y="0.5" width="13" height="13" fill="none" stroke="#fff"/><circle cx="7" cy="7" r="3.6" fill="none" stroke="#fff" stroke-width="0.9"/><ellipse cx="7" cy="7" rx="1.5" ry="3.6" fill="none" stroke="#fff" stroke-width="0.8"/><line x1="3.4" y1="7" x2="10.6" y2="7" stroke="#fff" stroke-width="0.8"/></svg>
        trhairexample.ca
      </li>
      <li>
        <svg viewBox="0 0 14 14" aria-hidden="true"><rect x="0.5" y="0.5" width="13" height="13" fill="none" stroke="#fff"/></svg>
        tr.hairstudio
      </li>
      <li>
        <svg viewBox="0 0 14 14" aria-hidden="true"><rect x="0.5" y="0.5" width="13" height="13" fill="none" stroke="#fff"/></svg>
        @TR_HairStudio
      </li>
    </ul>
  </section>

  <section class="card card--back" aria-label="Back of business card">
    <div class="wordmark">TR HAIR</div>
    <div class="appointment-title">Your Next Appointment</div>
    <svg class="appointment-rule" viewBox="0 0 304 10" aria-hidden="true">
      <line x1="0" y1="5" x2="304" y2="5" stroke="#474747" stroke-width="1"/>
      <rect x="149" y="2" width="6" height="6" fill="#000" transform="rotate(45 152 5)"/>
    </svg>
    <div class="slot slot--date">Date :<span class="slot__line"></span></div>
    <div class="slot slot--time">Time :<span class="slot__line"></span></div>
  </section>

</main>
</body>
</html>
```